Professional Business Card for Commercial Cleaning Company

We need a business card that represents our commercial janitorial cleaning company and represent several brands for our company so we do not want to highlight the logo too much. We want something that says we are professional.
Notes:No website or address as we have many locations and many websites and companies under our corporate name of "Brightvale Holdings, LLC" . Every time we hand a customer a business card they have contacted us via another brand we own but we don't want to have 21 business cards so we want to not focus on Brightvale Holdings, LLC too much since people will automatically ask "What is Brightvale Holdings, LLC" Example: Noodle Barn and Wrap Lantern restaurants are owned by "Zest! Brands" is the corporation name. Same principle here. Except we do not advertise at this time that all of our brands are connected. Hope this helps.
Target Market(s)
Commercial Cleaning
Industry/Entity Type
Janitorial Service
Contact Information for Business Card
Milo Jarvis
Business Development
555-382-9047
sales@brightvaleholdingsllc.example
Requirements
Must have
- Logo with contact information, need to be able to easily edit contact info for others in my office.
Nice to have
- Professional Image. Like to see a colorful bold look and a more standard business card look.
Should not have
- Any type of cleaning icons, tools, people or water.

```html
<!DOCTYPE html>
<html lang="en">
<head>
<meta charset="utf-8">
<title>Brightvale Holdings, LLC — Business Card</title>
<link rel="stylesheet" href="https://fonts.googleapis.com/css2?family=Poppins:wght@600&family=Saira+Semi+Condensed:wght@700&family=Open+Sans:wght@400&display=swap">
<style>
  :root {
    --navy: #1f3f82;
    --green: #6aa53f;
    --paper: #ffffff;
    --ink-soft: #5a6a8c;
    --backdrop: #e9ecef;
  }
  * { margin: 0; padding: 0; box-sizing: border-box; }
  html, body { width: 1200px; height: 900px; overflow: hidden; }
  body {
    background: var(--backdrop);
    position: relative;
  }
  .card {
    position: absolute;
    left: 320px;
    width: 560px;
    height: 320px;
    background: var(--paper);
    overflow: hidden;
    box-shadow: 0 6px 18px rgba(0,0,0,0.12);
  }
  .card--front { top: 110px; }
  .card--back { top: 470px; }
  .card__bands {
    position: absolute;
    inset: 0;
    width: 100%;
    height: 100%;
  }
  .brand-name {
    position: absolute;
    font-family: "Poppins", sans-serif;
    font-weight: 600;
    color: var(--navy);
    white-space: nowrap;
    letter-spacing: -0.3px;
  }
  .card--front .brand-name {
    left: 40px;
    top: 128px;
    font-size: 35px;
  }
  .card--back .brand-name {
    right: 30px;
    bottom: 42px;
    font-size: 21px;
  }
  .contact {
    position: absolute;
    left: 42px;
    top: 44px;
    color: var(--ink-soft);
  }
  .contact__name {
    font-family: "Saira Semi Condensed", sans-serif;
    font-weight: 700;
    font-size: 26px;
    color: var(--navy);
    line-height: 1;
  }
  .contact__title {
    font-family: "Open Sans", sans-serif;
    font-size: 12px;
    margin-top: 4px;
    letter-spacing: 0.3px;
  }
  .contact__lines {
    list-style: none;
    margin-top: 22px;
    font-family: "Open Sans", sans-serif;
    font-size: 13px;
    letter-spacing: 1px;
    line-height: 1.7;
  }
</style>
</head>
<body>

  <section class="card card--front" aria-label="Card front">
    <svg class="card__bands" viewBox="0 0 560 320" aria-hidden="true">
      <path d="M300 0 H560 V175 C470 110 390 55 300 0 Z" fill="var(--green)"/>
      <path d="M250 0 H278 C380 60 480 130 560 205 V232 C470 150 370 75 250 0 Z" fill="var(--navy)"/>
      <rect x="0" y="298" width="560" height="22" fill="var(--green)"/>
    </svg>
    <div class="brand-name">Brightvale Holdings, LLC</div>
  </section>

  <section class="card card--back" aria-label="Card back">
    <svg class="card__bands" viewBox="0 0 560 320" aria-hidden="true">
      <rect x="0" y="0" width="560" height="16" fill="var(--green)"/>
      <path d="M0 170 C110 230 200 280 290 320 H0 Z" fill="var(--green)"/>
      <path d="M0 128 C120 190 230 255 340 320 H312 C210 262 105 200 0 152 Z" fill="var(--navy)"/>
    </svg>
    <div class="contact">
      <h1 class="contact__name">Milo Jarvis</h1>
      <p class="contact__title">Business Development</p>
      <ul class="contact__lines">
        <li class="contact__phone">555-382-9047</li>
        <li class="contact__email">sales@brightvaleholdingsllc.example</li>
      </ul>
    </div>
    <div class="brand-name">Brightvale Holdings, LLC</div>
  </section>

</body>
</html>
```